Business Card design for Recruiter providing Recruitment Staff Augmentation services

I need a double sided business card. I have used Zek to print cards in the past and really like their quality. I have a logo but need to change the tagline that is part of the graphic.

The tagline currently reads and Connnecting people with careers - but it should be removed.

The back should look like a notecard for writing a to do list with the first to-do Augment Recruiting Staff

```html
<!DOCTYPE html>
<html lang="en">
<head>
<meta charset="utf-8">
<title>Crew Ascent – Business Card</title>
<link rel="stylesheet" href="https://fonts.googleapis.com/css2?family=Tinos:wght@400;700&display=swap">
<style>
  :root {
    --page-bg: #e4e5e7;
    --card-bg: #fbfbfb;
    --navy: #1d4466;
    --ink: #1b1b1b;
    --rust: #b5492e;
    --rule: #9fb3c4;
    --tint: #eef1f4;
  }
  * { box-sizing: border-box; margin: 0; padding: 0; }
  html, body { width: 1200px; height: 800px; overflow: hidden; }
  body {
    background: var(--page-bg);
    font-family: "Tinos", "Times New Roman", serif;
    color: var(--ink);
    position: relative;
  }
  .card {
    position: absolute;
    top: 250px;
    width: 525px;
    height: 300px;
    background: var(--card-bg);
    border-radius: 16px;
    box-shadow: 0 2px 8px rgba(0,0,0,.12);
    overflow: hidden;
  }
  .card-front { left: 45px; }
  .card-back { left: 630px; }

  /* Front */
  .brand {
    position: absolute;
    display: flex;
    align-items: center;
    gap: 12px;
  }
  .brand-front { left: 30px; top: 30px; }
  .brand-mark {
    border-radius: 50%;
    background: var(--navy);
    flex: none;
  }
  .brand-front .brand-mark { width: 40px; height: 40px; }
  .brand-name {
    color: var(--navy);
    font-weight: 700;
    letter-spacing: .04em;
    text-transform: uppercase;
    white-space: nowrap;
  }
  .brand-front .brand-name { font-size: 40px; }

  .person {
    position: absolute;
    left: 30px;
    top: 148px;
    width: 230px;
    text-align: right;
  }
  .person-name { font-size: 30px; letter-spacing: .03em; }
  .person-credential { font-size: 22px; color: var(--navy); letter-spacing: .06em; margin-top: 2px; padding-right: 4px; }

  .divider {
    position: absolute;
    left: 282px;
    top: 140px;
    width: 2px;
    height: 110px;
    background: var(--navy);
  }
  .contact {
    position: absolute;
    left: 300px;
    top: 160px;
    list-style: none;
    font-size: 18px;
    letter-spacing: .05em;
    line-height: 28px;
  }
  .contact li { display: flex; align-items: center; gap: 8px; }
  .contact svg { width: 13px; height: 13px; fill: var(--navy); flex: none; }

  /* Back */
  .back-decor {
    position: absolute;
    left: 60px;
    top: -20px;
    width: 230px;
    height: 230px;
    border-radius: 50%;
    background: var(--tint);
  }
  .todo-title {
    position: absolute;
    left: 30px;
    top: 22px;
    font-size: 18px;
    font-weight: 700;
  }
  .todo-lines {
    position: absolute;
    left: 30px;
    right: 30px;
    top: 54px;
    list-style: none;
  }
  .todo-lines li {
    height: 28px;
    border-bottom: 1px solid var(--rule);
    display: flex;
    align-items: flex-end;
    gap: 8px;
    padding-bottom: 3px;
    font-size: 16px;
  }
  .todo-check {
    width: 14px; height: 14px;
    background: var(--navy);
    border-radius: 2px;
    flex: none;
  }
  .tagline {
    position: absolute;
    left: 30px;
    bottom: 16px;
    font-size: 11px;
    color: var(--navy);
  }
  .brand-back { right: 26px; bottom: 14px; gap: 6px; }
  .brand-back .brand-mark { width: 14px; height: 14px; }
  .brand-back .brand-name { font-size: 16px; }
</style>
</head>
<body>

<section class="card card-front" aria-label="Business card front">
  <div class="brand brand-front">
    <span class="brand-mark"></span>
    <span class="brand-name">Crew Ascent</span>
  </div>

  <div class="person">
    <p class="person-name">Moo Zek</p>
    <p class="person-credential">SPHR</p>
  </div>

  <div class="divider"></div>

  <ul class="contact">
    <li>
      <svg viewBox="0 0 24 24" aria-hidden="true"><path d="M6.6 10.8a15.2 15.2 0 0 0 6.6 6.6l2.2-2.2c.3-.3.7-.4 1-.2 1.1.4 2.3.6 3.6.6.6 0 1 .4 1 1V20c0 .6-.4 1-1 1A17 17 0 0 1 3 4c0-.6.4-1 1-1h3.5c.6 0 1 .4 1 1 0 1.3.2 2.5.6 3.6.1.3 0 .7-.2 1z"/></svg>
      555-014-2290
    </li>
    <li>
      <svg viewBox="0 0 24 24" aria-hidden="true"><path d="M2 5h20v14H2z M2 5l10 8 10-8" /></svg>
      moo@crewascent.com
    </li>
    <li>
      <svg viewBox="0 0 24 24" aria-hidden="true"><circle cx="12" cy="12" r="10"/></svg>
      www.crewascent.com
    </li>
  </ul>
</section>

<section class="card card-back" aria-label="Business card back">
  <div class="back-decor"></div>
  <p class="todo-title">To do</p>
  <ul class="todo-lines">
    <li><span class="todo-check"></span>Augment Recruiting Staff</li>
    <li></li>
    <li></li>
    <li></li>
    <li></li>
    <li></li>
    <li></li>
  </ul>
  <p class="tagline">Connecting people with careers</p>
  <div class="brand brand-back">
    <span class="brand-mark"></span>
    <span class="brand-name">Crew Ascent</span>
  </div>
</section>

</body>
</html>
```